Startup Drone Platform Company business card

We are needing a business card design for our employees. We are a startup drone platform. We are looking for a business card that has our logo on one side, with the employee/company details on the opposite side. We are looking for something that is very eye catching, modern, and bold.

Target Market(s)

This will target both drone pilots and drone businesses, along with all the industries that could utilize drone services (aerial video, aerial photos, inspections, 3d mapping, etc).

Industry/Entity Type

Business

```html
<!DOCTYPE html>
<html lang="en">
<head>
<meta charset="utf-8">
<title>Velandro Business Card</title>
<link href="https://fonts.googleapis.com/css2?family=Montserrat:wght@400;500;700&display=swap" rel="stylesheet">
<style>
  :root {
    --backdrop: #3f8289;
    --card-black: #050505;
    --card-white: #ffffff;
    --accent: #3dbcc6;
    --ink: #111111;
  }
  * { margin: 0; padding: 0; box-sizing: border-box; }
  html, body { width: 1200px; height: 900px; overflow: hidden; }
  body {
    background: var(--backdrop);
    font-family: "Montserrat", sans-serif;
    position: relative;
  }
  .card {
    position: absolute;
    width: 700px;
    height: 400px;
    border-radius: 26px;
    overflow: hidden;
    box-shadow: 0 10px 24px rgba(0, 0, 0, 0.25);
  }
  .card--back { left: 110px; top: 40px; background: var(--card-black); }
  .card--front { left: 390px; top: 460px; background: var(--card-white); }

  .back-brand {
    position: absolute;
    left: 0; right: 0; top: 150px;
    display: flex; align-items: center; justify-content: center; gap: 18px;
    color: var(--accent);
    font-weight: 500;
    font-size: 40px;
    letter-spacing: 0.3em;
  }
  .back-brand .brand-name { margin-right: -0.3em; }
  .brand-dot {
    width: 22px; height: 22px; border-radius: 50%;
    border: 3px solid var(--accent);
    flex: none;
  }
  .back-url {
    position: absolute;
    left: 0; right: 0; bottom: 42px;
    text-align: center;
    color: #fff;
    font-size: 15px;
    font-weight: 500;
    letter-spacing: 0.28em;
  }
  .back-url .accent { color: var(--accent); }

  .front-brand {
    position: absolute;
    left: 50px; top: 48px;
    display: flex; align-items: center; gap: 10px;
    color: var(--ink);
    font-size: 24px;
    font-weight: 500;
    letter-spacing: 0.55em;
  }
  .front-brand .brand-dot { width: 16px; height: 16px; }
  .person { position: absolute; left: 50px; top: 150px; }
  .person-name { color: var(--accent); font-weight: 700; font-size: 34px; line-height: 1; }
  .person-role { color: var(--ink); font-size: 14px; margin-top: 6px; letter-spacing: 0.05em; }
  .address {
    position: absolute; left: 50px; top: 235px;
    font-size: 14px; line-height: 1.5; color: var(--ink); letter-spacing: 0.06em;
  }
  .contact { position: absolute; left: 50px; top: 290px; list-style: none; }
  .contact li {
    display: flex; align-items: center; gap: 14px;
    font-size: 14px; line-height: 26px; color: var(--ink); letter-spacing: 0.06em;
  }
  .contact svg { width: 14px; height: 14px; flex: none; }
</style>
</head>
<body>
  <section class="card card--back">
    <div class="back-brand"><span class="brand-dot"></span><span class="brand-name">VELANDRO</span></div>
    <p class="back-url">www.<span class="accent">velandro</span>.com</p>
  </section>

  <section class="card card--front">
    <div class="front-brand"><span>VELANDRO</span><span class="brand-dot"></span></div>
    <div class="person">
      <h1 class="person-name">John Doe</h1>
      <p class="person-role">Manager</p>
    </div>
    <p class="address">Harbor Lane Complex<br>Northfield, Westland 48210</p>
    <ul class="contact">
      <li>
        <svg viewBox="0 0 14 14"><rect x="3" y="1" width="8" height="12" rx="1.5" fill="none" stroke="var(--accent)" stroke-width="1.5"/></svg>
        555 0142 677
      </li>
      <li>
        <svg viewBox="0 0 14 14"><rect x="1" y="3" width="12" height="8" fill="none" stroke="var(--accent)" stroke-width="1.5"/><path d="M1 3 L7 8 L13 3" fill="none" stroke="var(--accent)" stroke-width="1.5"/></svg>
        info@velandro.com
      </li>
      <li>
        <svg viewBox="0 0 14 14"><circle cx="7" cy="7" r="6" fill="none" stroke="var(--accent)" stroke-width="1.5"/><path d="M1 7 H13 M7 1 C4 4 4 10 7 13 C10 10 10 4 7 1" fill="none" stroke="var(--accent)" stroke-width="1.2"/></svg>
        www.velandro.com
      </li>
    </ul>
  </section>
</body>
</html>
```